Poster for homelessness project (2 day deadline)

Amber Lantern Scheme is an initiative in the UK which aims to ensure that people who are new to sleeping on the street are quickly given assistance to take them out of situation they find themselves in.

It began as a London-based project but is now being rolled out nationwide. I am working for a project based in the north of England.

We need some posters which show an image of a place where a rough sleeper may spend the night with some supporting graphic design.

I have three initial images, but I need to be able to easily swap out the images for others. I would appreciate if you could produce three posters for me, each with a different image.

-
Please note:
My client is quite vague about what they want at the moment and the above words may change. I need the selected product to be a layered raw file that I can amend myself with any Adobe CS5.5 (or below) application.

Any typefaces that you choose need to be easily purchasable online.

Please view formatinfo.pdf for formatting guidelines.

Target Market(s)

The general public. It will be placed in public places.

Industry/Entity Type

Graphic Design

Requirements
Must have
• Must contain the words:

"Tonight someone will sleep rough for the first time. Help us make sure they find the Amber Lantern."

"Would you sleep here? Sleeping rough is dangerous. Make sure everyone finds the Amber Lantern."

-
Nice to have
• I'd like this to be quite bleak, grimy and "urban" in feel.

You may recolour/tint the images in any way to enhance this feeling.

```html
<!DOCTYPE html>
<html lang="en">
<head>
<meta charset="utf-8">
<title>Amber Lantern Scheme – Would you sleep here? poster series</title>
<link rel="stylesheet" href="https://fonts.googleapis.com/css2?family=PT+Sans+Narrow:wght@400;700&display=swap">
<style>
  :root {
    --backdrop: #cbb99a;
    --headline-red: #9a1a1a;
    --lead-bold: #e8dcc6;
    --lead-regular: #d2c5b0;
    --footer-text: #ebe2d2;
    --panel-white: #ffffff;
    --sepia-pale: #bfae97;
    --sepia-light: #9c8a74;
    --sepia-mid: #6a5a4a;
    --sepia-deep: #463a30;
    --sepia-dark: #2a221c;
    --sepia-black: #14100d;
  }
  html, body {
    margin: 0;
    padding: 0;
    width: 1200px;
    height: 608px;
    overflow: hidden;
    background: var(--backdrop);
  }
  .poster-series {
    position: relative;
    width: 1200px;
    height: 608px;
  }
  .poster {
    position: absolute;
    top: 67px;
    width: 342px;
    height: 478px;
    box-shadow: 5px 6px 6px rgba(0, 0, 0, 0.45);
    overflow: hidden;
    font-family: "PT Sans Narrow", "Arial Narrow", sans-serif;
    background: var(--sepia-black);
  }
  .poster--doorway { left: 53px; }
  .poster--bins { left: 425px; }
  .poster--bench { left: 796px; }

  .poster__photo {
    position: absolute;
    inset: 0;
  }
  /* Doorway: pale whitewashed wall on the left, dark steel door on the right, sign band at top */
  .poster--doorway .poster__photo {
    background:
      radial-gradient(ellipse 120% 100% at 40% 45%, transparent 55%, rgba(20,16,13,0.7) 100%),
      linear-gradient(180deg, rgba(200,186,165,0.55) 0%, rgba(200,186,165,0.4) 12%, rgba(60,50,42,0.55) 15%, transparent 24%, transparent 86%, rgba(20,16,13,0.85) 100%),
      linear-gradient(90deg, var(--sepia-mid) 0%, var(--sepia-pale) 12%, #b3a28b 40%, #8e7d69 52%, var(--sepia-dark) 55%, #3a302a 70%, #2f2620 88%, #4a3e34 94%, var(--sepia-dark) 100%);
  }
  /* Back alley: dark brick above, grey-brown bins across the middle, black ground */
  .poster--bins .poster__photo {
    background:
      radial-gradient(ellipse 120% 100% at 50% 50%, transparent 50%, rgba(14,11,9,0.75) 100%),
      linear-gradient(180deg, var(--sepia-dark) 0%, #3d332b 20%, #55483c 36%, #7a6a58 46%, #6e5e4e 62%, #4f4236 76%, var(--sepia-dark) 88%, var(--sepia-black) 100%),
      linear-gradient(90deg, #2e2620 0%, transparent 30%, transparent 70%, #2e2620 100%);
    background-blend-mode: normal, multiply, normal;
  }
  /* Park: fog glowing top-left, dark tree and bench to the right, shadowed path below */
  .poster--bench .poster__photo {
    background:
      radial-gradient(ellipse 70% 45% at 25% 38%, rgba(196,180,158,0.75) 0%, transparent 70%),
      radial-gradient(ellipse 55% 60% at 95% 20%, rgba(24,19,15,0.85) 0%, transparent 70%),
      linear-gradient(180deg, #8f7d69 0%, #a3917b 30%, #8c7a66 50%, var(--sepia-deep) 66%, var(--sepia-dark) 84%, var(--sepia-black) 100%),
      linear-gradient(90deg, transparent 55%, rgba(20,16,13,0.6) 100%);
    background-blend-mode: normal, normal, multiply, normal;
  }

  .poster__lead {
    position: absolute;
    left: 30px;
    top: 89px;
    margin: 0;
    font-size: 15px;
    line-height: 18px;
    letter-spacing: -0.1px;
  }
  .poster__lead strong {
    display: block;
    font-weight: 700;
    color: var(--lead-bold);
  }
  .poster__lead span {
    display: block;
    font-weight: 400;
    color: var(--lead-regular);
  }
  .poster__headline {
    position: absolute;
    left: 30px;
    top: 146px;
    margin: 0;
    font-size: 34px;
    line-height: 31px;
    font-weight: 700;
    letter-spacing: -0.8px;
    color: var(--headline-red);
  }
  .poster--bins .poster__headline { top: 139px; }
  .poster__headline span { display: block; }
  .poster__headline span + span { padding-left: 29px; }

  .poster__footer {
    position: absolute;
    left: 11px;
    right: 9px;
    top: 424px;
    margin: 0;
    font-size: 12px;
    color: var(--footer-text);
  }
  .poster__sponsor-panel {
    position: absolute;
    left: 9px;
    right: 9px;
    top: 444px;
    height: 24px;
    background: var(--panel-white);
  }
</style>
</head>
<body>
<main class="poster-series">

  <article class="poster poster--doorway">
    <div class="poster__photo" role="img" aria-label="Grimy sepia photograph of a locked nightclub back door set in a whitewashed wall"></div>
    <p class="poster__lead"><strong>Tonight someone will sleep rough for the first time.</strong><span>Help us make sure they find the Amber Lantern.</span></p>
    <h2 class="poster__headline"><span>Would you</span><span>sleep here?</span></h2>
    <p class="poster__footer">Sleeping rough is dangerous. Make sure everyone finds the Amber Lantern.</p>
    <div class="poster__sponsor-panel"></div>
  </article>

  <article class="poster poster--bins">
    <div class="poster__photo" role="img" aria-label="Grimy sepia photograph of graffiti-covered wheelie bins against a brick back-alley wall"></div>
    <p class="poster__lead"><strong>Tonight someone will sleep rough for the first time.</strong><span>Help us make sure they find the Amber Lantern.</span></p>
    <h2 class="poster__headline"><span>Would you</span><span>sleep here?</span></h2>
    <p class="poster__footer">Sleeping rough is dangerous. Make sure everyone finds the Amber Lantern.</p>
    <div class="poster__sponsor-panel"></div>
  </article>

  <article class="poster poster--bench">
    <div class="poster__photo" role="img" aria-label="Bleak sepia photograph of a wooden park bench beside a foggy tree-lined path"></div>
    <p class="poster__lead"><strong>Tonight someone will sleep rough for the first time.</strong><span>Help us make sure they find the Amber Lantern.</span></p>
    <h2 class="poster__headline"><span>Would you</span><span>sleep here?</span></h2>
    <p class="poster__footer">Sleeping rough is dangerous. Make sure everyone finds the Amber Lantern.</p>
    <div class="poster__sponsor-panel"></div>
  </article>

</main>
</body>
</html>
```